Book cover for a book about time management for women

We need a book cover for a book about time management for women written by a woman. Even though the book has a provocative title "Calendar candy" based on the seminars the author holds for women seeking the change in their life, it has nothing to do with the words themselves. The subtitle is "Keep each morning in your grip. A bold guide on daily rhythm for ladies today"

Preferred fonts (not necessarily):
Plus Jakarta Sans
Tiempos Headline

Preferred colours (not necessarily):
- orange
- pastel "highlighters"

We look for a simple/clean design that catches the attention of the women without too many graphic elements.

Target Market(s)

Women that want to change and organise their life

Industry/Entity Type

productivity, marketing, work-life balance

Font styles to use
Other font styles liked:
• Plus Jakarta Sans, Tiempos Headline

Colors
F0912C
F2A743
F7CA91
FBE8D2
FDF5EE
A7469A
B969AE
D3A5CF
EDDBEB
F8F0F9

Requirements
Must have
• Famine feeling as the target audience are women with drive to better life
Should not have
• No explicit images or sexually motivated themes

```html
<!DOCTYPE html>
<html lang="en">
<head>
<meta charset="utf-8">
<title>Calendar Candy – Book Front</title>
<link href="https://fonts.googleapis.com/css2?family=Cinzel:wght@500&family=Plus+Jakarta+Sans:wght@700&family=Libre+Caslon+Text&display=swap" rel="stylesheet">
<style>
  :root {
    --orange-deep: #F0912C;
    --orange: #F2A743;
    --orange-soft: #F7CA91;
    --plum: #A7469A;
    --orchid: #B969AE;
    --lilac: #D3A5CF;
    --ink: #666666;
    --ink-soft: #808080;
    --numeral: #E6E6E6;
    --paper: #FFFFFF;
    --backdrop: #EDEDED;
  }
  * { margin: 0; padding: 0; box-sizing: border-box; }
  html, body {
    width: 849px; height: 1200px; overflow: hidden;
    background: var(--backdrop);
  }
  .book-front {
    position: absolute;
    left: 34px; top: 15px;
    width: 780px; height: 1170px;
    background: var(--paper);
    box-shadow: 0 6px 24px rgba(0,0,0,0.18);
    overflow: hidden;
  }
  .cover-art {
    position: absolute; inset: 0;
    width: 780px; height: 1170px;
  }
  .title {
    position: absolute; left: 0; right: 0; top: 88px;
    text-align: center;
    font-family: "Cinzel", "Times New Roman", serif;
    font-weight: 500;
    font-size: 54px;
    line-height: 1;
    letter-spacing: 3px;
    color: var(--ink);
  }
  .subtitle {
    position: absolute; left: 0; right: 0; top: 153px;
    text-align: center;
    font-family: "Plus Jakarta Sans", Arial, sans-serif;
    font-weight: 700;
    font-size: 32px;
    line-height: 1;
    letter-spacing: 5px;
    color: var(--ink-soft);
  }
  .author {
    position: absolute; left: 0; right: 0; top: 1088px;
    text-align: center;
    font-family: "Plus Jakarta Sans", Arial, sans-serif;
    font-weight: 700;
    font-size: 33px;
    line-height: 1;
    letter-spacing: 6.5px;
    color: var(--ink);
  }
  .numeral {
    font-family: "Libre Caslon Text", "Times New Roman", serif;
    font-size: 262px;
    fill: var(--numeral);
  }
  .clock-arc { fill: none; stroke: var(--ink-soft); stroke-width: 4; stroke-linecap: round; stroke-linejoin: round; }
  .band-orange { fill: var(--orange); }
  .band-lilac { fill: var(--lilac); }
  .butterfly-deep { fill: var(--plum); }
  .butterfly-pink { fill: #C865AC; }
</style>
</head>
<body>
  <main class="book-front">
    <svg class="cover-art" viewBox="0 0 780 1170" xmlns="http://www.w3.org/2000/svg">
      <defs>
        <linearGradient id="sofa-tones" x1="0" y1="0" x2="1" y2="1">
          <stop offset="0" stop-color="#F7CA91"/>
          <stop offset="0.4" stop-color="#F2A743"/>
          <stop offset="0.62" stop-color="#D3A5CF"/>
          <stop offset="1" stop-color="#F0912C"/>
        </linearGradient>
        <clipPath id="clock-face">
          <circle cx="388" cy="564" r="309"/>
        </clipPath>
      </defs>

      <text class="numeral" x="342" y="446" textLength="279" lengthAdjust="spacingAndGlyphs">XII</text>

      <path role="img" aria-label="Illustration of a woman in a lilac dress relaxing on an orange sofa"
            clip-path="url(#clock-face)"
            fill="url(#sofa-tones)"
            d="M60 468 L97 468 L194 334 L300 345 L390 405 L480 545 L630 690 L700 700 L700 900 L60 900 Z"/>

      <path class="clock-arc" d="M403 253 A311 311 0 1 0 699 565"/>
      <path class="clock-arc" d="M390 245 L403 253 L390 261"/>
      <path class="clock-arc" d="M691 577 L699 563 L707 577"/>

      <path class="band-lilac" d="M0 1030 C100 990 250 970 400 982 C550 995 650 1025 780 1027 L780 1066 C660 1072 560 1050 440 1030 C300 1005 150 990 0 1022 Z"/>
      <path class="band-orange" d="M0 983 C180 980 330 1020 480 1035 C600 1045 700 1010 780 984 L780 1010 C680 1030 560 1050 450 1045 C300 1035 150 1000 60 1005 C30 1008 10 1012 0 1016 Z"/>

      <ellipse class="butterfly-deep" role="img" aria-label="Small purple butterfly" cx="273" cy="1012" rx="20" ry="15"/>
      <ellipse class="butterfly-pink" role="img" aria-label="Small pink butterfly" cx="551" cy="986" rx="18" ry="14"/>
    </svg>

    <h1 class="title">CALENDAR CANDY</h1>
    <p class="subtitle">Keep Each Morning In Your Grip</p>
    <p class="author">Author : Mara Kolen</p>
  </main>
</body>
</html>
```